Brochure Design Project

12pp DL brochure/booklet (6 sheets double sided DL size):

16pp DL brochure/booklet (8 sheets double sided DL size):

I need a new Price Menu Booklet for my combined Hair Salon and Day Spa. We are part of the LUMORA network, so the look has to be Modern, Eco-Friendly but not overly Avante-Garde.

Depending on layout the booklet should be no more than 8 double sided sheets. I willprovide the content but not the images. I have provided a .pdf example of the booklet we did a couple of year ago.

The inside front cover will also include a " coupon / voucher" design to invite new clients with a $20 money off promotion. The rest of the booklet with be prices, services and our contact details.

Finished Art Work must be print ready for my local printer.
Updates

PLEASE LOOK AT THE 2 .PDF EXAMPLES ATTACHED WHICH HAVE THE LOOK AND FEEL OF THE DESIGN I WANT.

The Offer to New Clients MUST be designed to appear like a Gift Voucher or Coupon.

Target Market(s)

Mostly female. Late Teen's through to Seniors. Local area is a mixture of White Anglo Saxon / Mediterranean / Asian / Arabic cultures

Industry/Entity Type

Hair

Requirements
Must have
• Salon Logo on the Front Cover (aesthetics )

Hair Salon Partners Logo's - Pirex and Lumora in the Hair Salon related section

Spa Salon Partners Logo's - Dermavelle / Lumora / Nail-Crest in the Spa related section
Nice to have
• PLEASE LOOK AT THE 2 .PDF EXAMPLES ATTACHED WHICH HAVE THE LOOK AND FEEL OF THE DESIGN I WANT.

Should not have
• " Cheap " Looking images

```html
<!DOCTYPE html>
<html lang="en">
<head>
<meta charset="utf-8">
<title>Lumora Salon &amp; Spa — Price Menu Pages 11–14</title>
<link rel="stylesheet" href="https://fonts.googleapis.com/css2?family=Parisienne&family=Jost:wght@400;500&family=EB+Garamond:ital,wght@1,600;1,700&display=swap">
<style>
  :root {
    --backdrop: #e6e3df;
    --paper: #ffffff;
    --paper-grey: #f1f0ef;
    --ink: #3a3a3a;
    --ink-soft: #5a5a5a;
    --accent: #c8281f;
    --photo-skin: #e8cbb4;
    --photo-light: #f6f1ec;
    --photo-stone-top: #ecebea;
    --photo-stone-bottom: #dcdad8;
    --shadow: rgba(0,0,0,0.18);
  }
  * { box-sizing: border-box; margin: 0; padding: 0; }
  html, body { width: 1200px; height: 1000px; overflow: hidden; }
  body {
    background: var(--backdrop);
    font-family: "Jost", "Futura", sans-serif;
    color: var(--ink);
    position: relative;
  }
  .spread {
    position: absolute;
    top: 197px;
    width: 570px;
    height: 605px;
    display: flex;
    box-shadow: 0 10px 30px var(--shadow);
  }
  .spread--massage { left: 22px; }
  .spread--services { left: 608px; }
  .page {
    width: 285px;
    height: 100%;
    background: var(--paper);
    position: relative;
    overflow: hidden;
  }
  .page + .page { border-left: 1px solid #e4e4e4; }
  .photo {
    height: 180px;
    width: 100%;
  }
  .photo--stones {
    background: linear-gradient(120deg, var(--photo-light) 0%, var(--photo-skin) 55%, var(--photo-light) 100%);
  }
  .photo--flowers {
    background: linear-gradient(200deg, var(--photo-light) 0%, #e6c3ac 60%, var(--photo-light) 100%);
  }
  .page__body { padding: 12px 20px 0; position: relative; }
  .section-title {
    font-family: "Parisienne", cursive;
    color: var(--accent);
    font-weight: 400;
    font-size: 23px;
    line-height: 1.1;
    margin-bottom: 10px;
    white-space: nowrap;
  }
  .treatment { margin-bottom: 11px; }
  .treatment__name {
    font-size: 8.6px;
    text-transform: uppercase;
    letter-spacing: 0.3px;
    font-weight: 500;
  }
  .treatment__tagline {
    font-family: "EB Garamond", serif;
    font-style: italic;
    font-weight: 700;
    text-transform: none;
    font-size: 9.5px;
  }
  .treatment__desc {
    font-size: 8.4px;
    line-height: 1.35;
    color: var(--ink-soft);
    margin-top: 2px;
  }
  .price {
    text-align: right;
    font-size: 8.4px;
    color: var(--ink-soft);
    margin-top: 2px;
  }
  .price b {
    font-family: "EB Garamond", serif;
    font-style: italic;
    font-weight: 700;
    font-size: 10.5px;
    color: var(--ink);
  }
  .note {
    font-family: "EB Garamond", serif;
    font-style: italic;
    font-weight: 700;
    font-size: 9.5px;
  }
  .page--grey { background: var(--paper-grey); }
  .stones-backdrop {
    position: absolute;
    inset: 0;
    background: linear-gradient(180deg, var(--photo-stone-top) 0%, var(--photo-stone-bottom) 100%);
  }
  .centered { text-align: center; }
  .loyalty__heading {
    color: var(--accent);
    font-size: 7.8px;
    text-transform: uppercase;
    letter-spacing: 0.4px;
    margin: 8px 0 2px;
    text-align: center;
  }
  .loyalty__text {
    font-size: 7.8px;
    line-height: 1.35;
    color: var(--ink-soft);
    text-align: center;
  }
  .sign-off {
    color: var(--accent);
    font-family: "EB Garamond", serif;
    font-style: italic;
    font-weight: 700;
    font-size: 9.5px;
    text-align: center;
    margin-top: 10px;
  }
  .packages-title { margin-top: 46px; }
  .loyalty-title { font-size: 21px; margin: 14px 0 2px; }
</style>
</head>
<body>

<section class="spread spread--massage">
  <article class="page">
    <div class="photo photo--stones" role="img" aria-label="Photo of a woman receiving a hot stone massage beside candles"></div>
    <div class="page__body">
      <h2 class="section-title">stress-relieving massage (cont)</h2>
      <div class="treatment">
        <p class="treatment__name">Chakra Balancing Massage – <span class="treatment__tagline">balance your senses</span></p>
        <p class="treatment__desc">The concept of Chakras comes from Ayurveda, the ancient healing art of India. These 7 energy centres are located along the spine and can be thought of as personal growth centres that connect your sub conscious with your physical body. The Chakra Balancing Massage seeks to create harmony in the Chakra System using a variety of massage techniques – Deep Tissue, Chakra Foot Reflexology and Chakra Energy work.</p>
        <p class="price">1hr <b>86</b></p>
      </div>
      <div class="treatment">
        <p class="treatment__name">Hot Stone Massage – <span class="treatment__tagline">absolute relaxation to warm the soul</span></p>
        <p class="treatment__desc">Experience the aromatic power of plant pure-fumes fused with the sensation of smooth warm stones. Alternating stones comfort, destress and melt muscle tension.</p>
        <p class="price">1hr <b>115</b> 1.5hrs <b>151</b></p>
      </div>
      <div class="treatment">
        <p class="treatment__name">Remedial Massage</p>
        <p class="treatment__desc">Marco, Our Male Masseur is available for guests requiring a deep tissue, remedial massage.</p>
        <p class="price">from <b>100</b></p>
      </div>
    </div>
  </article>
  <article class="page">
    <div class="photo photo--flowers" role="img" aria-label="Photo of a relaxed woman with flowers in her hair"></div>
    <div class="page__body">
      <h2 class="section-title">spa body treatments</h2>
      <div class="treatment">
        <p class="treatment__name">Aqua Salt Glow</p>
        <p class="treatment__desc">A skin-refining body treatment using natural minerals and sea salts enhanced with a personalised, aromatic Lumora essential oil. The result is soft and smooth polished skin.</p>
        <p class="price">45min <b>70</b></p>
      </div>
      <div class="treatment">
        <p class="treatment__name">Essential Back Treatment – <span class="treatment__tagline">facial for the back</span></p>
        <p class="treatment__desc">The hard-to-reach area of your back is tended to during this deep-cleansing masque and massage. Shoulders, neck and back are purified and refined to ensure well cared for skin all over.</p>
        <p class="price">30 min <b>56</b></p>
      </div>
      <div class="treatment">
        <p class="treatment__name">Rosemary Mint Body Wrap – <span class="treatment__tagline">awaken your senses</span></p>
        <p class="treatment__desc">Renew both body and mind. Your body is exfoliated, wrapped and warmed. Essences of rosemary and mint awaken your senses and leave skin refreshed.</p>
        <p class="price">1hr <b>95</b></p>
      </div>
      <div class="treatment">
        <p class="treatment__name">Caribbean Therapy – <span class="treatment__tagline">deluxe style</span></p>
        <p class="treatment__desc">A rejuvenating treatment that uses the best of the Caribbean seaweeds and minerals, followed by a soothing massage to finish.</p>
        <p class="price">1.5hrs <b>140</b></p>
      </div>
    </div>
  </article>
</section>

<section class="spread spread--services">
  <article class="page page--grey">
    <div class="page__body">
      <h2 class="section-title">special services</h2>
      <div class="treatment">
        <p class="treatment__name">Fat Cavitation – Non-Invasive Cellulite Reduction</p>
        <p class="note">See separate brochure for our competitive pricing.</p>
      </div>
      <div class="treatment">
        <p class="treatment__name">LED Light (Add-on to a Facial)</p>
        <p class="treatment__desc">Light Therapy increases the production of collagen, triggering repair mechanisms and stimulating cell growth. It can addresses Acne and reduces pigmentation naturally.</p>
        <p class="price"><b>25 LED</b></p>
      </div>
      <div class="treatment">
        <p class="treatment__name">Collagen Eye Treatment</p>
        <p class="treatment__desc">Reduces dark circles, puffiness and fine lines.</p>
        <p class="price"><b>21</b></p>
      </div>
      <div class="treatment">
        <p class="treatment__name">Collagen Masque Treatment</p>
        <p class="treatment__desc">Visibly improves skin Hydration leaving the skin fresh and toned.</p>
        <p class="price"><b>40</b></p>
      </div>
      <div class="treatment">
        <p class="treatment__name">Dermavelle Peels</p>
        <p class="treatment__desc">Peels are a form of resurfacing. Treatments are great for pigmentation, congestion, breakouts, epidermal skin thickening, dehydration &amp; anti-aging.</p>
        <p class="price"><b>26 - 250</b></p>
      </div>
      <div class="treatment">
        <p class="treatment__name">Ear Candling</p>
        <p class="treatment__desc">Ear Candling induces a pleasant feeling of warmth and a balance of pressure in the ear whilst drawing out excessive wax and congestion within the sinuses.</p>
        <p class="price"><b>66</b></p>
      </div>
      <div class="treatment">
        <p class="treatment__name">Botanical Hair &amp; Scalp Therapy</p>
        <p class="treatment__desc">A tension relieving, balancing scalp treatment and intense repairing "facial" for hair. Can be incorporated into any facial or body treatment.</p>
        <p class="price"><b>51</b></p>
      </div>
    </div>
  </article>
  <article class="page page--grey">
    <div class="stones-backdrop" role="img" aria-label="Faded background photo of stacked spa stones with a coral leaf"></div>
    <div class="page__body">
      <h2 class="section-title packages-title">packages</h2>
      <p class="treatment__desc">Let us take the hard work out of creating a package for that special person.</p>
      <div class="treatment" style="margin-top:8px">
        <p class="treatment__name">Total Body Indulgence</p>
        <p class="treatment__desc">Following an eyebrow wax and lash and brow tint, your total body indulgence begins with a foot soak and exfoliation of the feet. Relax with a one hour facial customized to suit your specific needs, including foot massage. Your journey continues with a back exfoliation and soothing back massage. Complete this beautiful experience with complimentary Finishing Touch makeup application.</p>
        <p class="price">2hrs <b>175</b></p>
      </div>
      <h2 class="section-title centered loyalty-title">customer loyalty club</h2>
      <p class="loyalty__heading">We love to reward loyalty</p>
      <p class="loyalty__text">Every service &amp; every product purchase you make earns points in our loyalty program. Your points can be redeemed against services whenever you decide. (Points valid 12 months from earn day)</p>
      <p class="loyalty__heading">Cancellation Policy</p>
      <p class="loyalty__text">New clients booking Spa treatments over $100 are required to provide credit card details to confirm appointments. If you are unable to make your appointment kindly provide a minimum of 24 hours notice so that we can give our time to others. We reserve the right to charge a $50 'no show' fee if 24 hours notice is not provided.</p>
      <p class="loyalty__heading">15% Discount* off Spa Treatments<br>Every Tuesday</p>
      <p class="loyalty__text">*Excludes Packages / Eye Lash Extensions / Current Special Offers / Remedial Massage / Nail-Crest. Not available with any other offer and subject to change. Discount not available during some Holiday periods, see in store for details.</p>
      <p class="sign-off">If you are happy, tell others. If not, tell us!</p>
    </div>
  </article>
</section>

</body>
</html>
```